Business card design needed

we are a bakery that specialises in traditional sourdough breads all shaped by hand. we are a little rustic but cater to a wide variety of people and are based in an affluent suburb. i think i would prefer lighter earthy colours. with some dark colours like bread crust maybe.

Industry/Entity Type

Bakery

Contact Information for Business Card

MAPLE HEARTH BAKERY
382 CARLOW RD
SURREY HILLS
VIC 3127
PH: 03 95517204
EMAIL: maplehearth@kestrelmail.com.au

Requirements
Must have
• no photos. hand drawing would be great

```html
<!DOCTYPE html>
<html lang="en">
<head>
<meta charset="utf-8">
<title>Maple Hearth Bakery – Business Card</title>
<link rel="stylesheet" href="https://fonts.googleapis.com/css2?family=Arimo:wght@400;700&family=Architects+Daughter&display=swap">
<style>
  :root {
    --card-cream: #f8e1b8;
    --crust-brown: #ad5c2e;
    --ink: #111111;
    --flour-white: #ffffff;
  }
  html, body {
    margin: 0;
    padding: 0;
    width: 1200px;
    height: 693px;
    overflow: hidden;
    background: var(--card-cream);
  }
  .card {
    position: relative;
    width: 1200px;
    height: 693px;
    background: var(--card-cream);
    font-family: "Arimo", Helvetica, Arial, sans-serif;
    color: var(--ink);
  }
  .tagline-band {
    position: absolute;
    left: 0;
    top: 115px;
    width: 532px;
    height: 122px;
    background: var(--crust-brown);
  }
  .tagline {
    position: absolute;
    left: 164px;
    top: 12px;
    margin: 0;
    font-family: "Architects Daughter", cursive;
    font-size: 42px;
    line-height: 46px;
    letter-spacing: 4px;
    color: var(--flour-white);
    text-transform: uppercase;
  }
  .brand {
    position: absolute;
    left: 700px;
    top: 130px;
    width: 440px;
    text-align: center;
  }
  .brand-name {
    margin: 0;
    font-family: "Arimo", Helvetica, Arial, sans-serif;
    font-weight: 700;
    font-size: 44px;
    line-height: 62px;
    letter-spacing: 3px;
    color: var(--ink);
  }
  .contact-icon {
    position: absolute;
    left: 105px;
    width: 70px;
  }
  .contact-icon svg { display: block; width: 70px; height: 100%; }
  .icon-home { top: 370px; height: 67px; }
  .icon-phone { top: 502px; height: 60px; }
  .icon-mail { top: 595px; height: 45px; }
  .icon-shape { fill: var(--crust-brown); }
  .contact-text {
    position: absolute;
    left: 217px;
    margin: 0;
    font-size: 42px;
    font-weight: 400;
    line-height: 64px;
    white-space: nowrap;
  }
  .text-address { top: 365px; }
  .text-phone { top: 506px; }
  .text-email { top: 578px; }
</style>
</head>
<body>
  <main class="card">
    <div class="tagline-band">
      <p class="tagline">Freshly<br>Baked!</p>
    </div>

    <div class="brand">
      <p class="brand-name">MAPLE HEARTH<br>BAKERY</p>
    </div>

    <span class="contact-icon icon-home">
      <svg viewBox="0 0 70 67" aria-hidden="true">
        <path class="icon-shape" d="M35 2 L1 34 H11 V67 H28 V46 H42 V67 H59 V34 H69 L57 23 V8 H49 V15 Z"/>
      </svg>
    </span>
    <p class="contact-text text-address">382 Carlow Rd<br>Ashby Vale VIC 3184</p>

    <span class="contact-icon icon-phone">
      <svg viewBox="0 0 70 60" aria-hidden="true">
        <path class="icon-shape" d="M12 1 C8 1 1 7 1 16 C1 36 25 59 46 59 C54 59 60 53 60 49 C60 46 50 39 46 39 C43 39 41 43 38 43 C32 43 20 31 20 25 C20 22 24 20 24 17 C24 13 16 1 12 1 Z"/>
      </svg>
    </span>
    <p class="contact-text text-phone">(03) 9551 7204</p>

    <span class="contact-icon icon-mail">
      <svg viewBox="0 0 70 45" aria-hidden="true">
        <path class="icon-shape" d="M1 1 H69 L35 24 Z"/>
        <path class="icon-shape" d="M1 8 L35 31 L69 8 V45 H1 Z"/>
      </svg>
    </span>
    <p class="contact-text text-email">maplehearth@kestrelmail.com.au</p>
  </main>
</body>
</html>
```